Now Accepting upcoming Consignment's for our up coming online Farm And Construction Equipment Auction April 14-17th
Consign Now
Commission Rates per item
$1-$500 10%
$501-$7000 8%
$ 7000 and up Flat $ 500 fee per item
Many Items Contact us For Custom Commission Rates
Contact Garrett At (555)-214-7630, Garrett@kemplerauction.com
Cant Get It here we offer trucking

```html
<!DOCTYPE html>
<html lang="en">
<head>
<meta charset="utf-8">
<title>Kempler Auction Service – Upcoming Consignments</title>
<link href="https://fonts.googleapis.com/css2?family=Oswald:wght@500;600;700&family=Roboto:wght@400;500;700&display=swap" rel="stylesheet">
<style>
  :root {
    --frame: #d9dadb;
    --card: #ffffff;
    --ink: #1d1f22;
    --orange: #f28c1e;
    --sky-top: #eef3f6;
    --sky-low: #dfe9ef;
    --field: #7a5a3a;
    --green: #1f5a2a;
    --white: #ffffff;
  }
  * { box-sizing: border-box; margin: 0; padding: 0; }
  html, body { width: 755px; height: 1200px; overflow: hidden; background: var(--frame); }
  .flyer {
    position: absolute; left: 15px; top: 15px; width: 725px; height: 1170px;
    background: var(--card); overflow: hidden;
    font-family: "Roboto", Arial, sans-serif; color: var(--ink);
  }
  .hero {
    position: absolute; left: 0; top: 0; width: 100%; height: 735px;
    background: linear-gradient(180deg, var(--sky-top) 0%, #f7f9fa 45%, var(--sky-low) 55%);
  }
  .brand {
    position: absolute; top: 26px; left: 0; width: 100%;
    display: flex; flex-direction: column; align-items: center; gap: 4px;
  }
  .brand-dot { width: 48px; height: 48px; border-radius: 50%; background: var(--orange); }
  .brand-name {
    font-family: "Oswald", Arial, sans-serif; font-weight: 600; font-size: 20px;
    letter-spacing: 1px; color: var(--ink); text-transform: uppercase;
  }
  .headline {
    position: absolute; top: 122px; width: 100%; text-align: center; white-space: nowrap;
    font-family: "Oswald", Arial, sans-serif; font-weight: 700; font-size: 35px;
    text-transform: uppercase; letter-spacing: 0;
  }
  .auction-banner {
    position: absolute; top: 178px; left: 80px; width: 565px; height: 82px;
    background: var(--orange); border-radius: 10px;
    display: flex; align-items: center; justify-content: center; text-align: center;
    font-family: "Oswald", Arial, sans-serif; font-weight: 600; font-size: 29px; line-height: 1.15;
    color: var(--white); text-transform: uppercase;
  }
  .intro {
    position: absolute; top: 272px; left: 115px; width: 495px; text-align: center;
    font-size: 23px; line-height: 1.3;
  }
  .equipment-photo {
    position: absolute; left: 0; top: 345px; width: 100%; height: 390px;
    background: linear-gradient(180deg, #dbe6ec 0%, #c9d7a8 30%, #9a7a52 62%, var(--field) 100%);
  }
  .online-tag {
    position: absolute; left: 0; top: 640px; width: 100%; text-align: center;
    font-family: "Oswald", Arial, sans-serif; font-weight: 500; font-size: 30px;
    color: var(--white); text-transform: uppercase; letter-spacing: 0.5px;
    text-shadow: 0 1px 4px rgba(0,0,0,0.45);
  }
  .rates-title {
    position: absolute; top: 752px; width: 100%; text-align: center;
    font-family: "Oswald", Arial, sans-serif; font-weight: 700; font-size: 32px; text-transform: uppercase;
  }
  .rates-table {
    position: absolute; top: 805px; left: 95px; width: 535px;
    border-collapse: collapse; font-size: 21px;
  }
  .rates-table th, .rates-table td {
    border: 1.5px solid var(--ink); height: 40px; text-align: center; padding: 0 8px;
  }
  .rates-table th { font-weight: 500; }
  .custom-rates {
    position: absolute; top: 980px; width: 100%; text-align: center;
    font-family: "Oswald", Arial, sans-serif; font-weight: 700; font-size: 27px; text-transform: uppercase;
  }
  .custom-rates .accent { color: var(--orange); }
  .consign-button {
    position: absolute; top: 1028px; left: 235px; width: 255px; height: 48px;
    background: var(--orange); border-radius: 8px; color: var(--white);
    display: flex; align-items: center; justify-content: center;
    font-family: "Oswald", Arial, sans-serif; font-weight: 600; font-size: 27px; text-transform: uppercase;
  }
  .more-items {
    position: absolute; top: 1084px; left: 60px; width: 605px; text-align: center;
    font-size: 18px; line-height: 1.3;
  }
  .contact-bar {
    position: absolute; left: 0; bottom: 0; width: 100%; height: 38px; background: var(--green);
    display: flex; align-items: center; justify-content: center; gap: 48px;
    color: var(--white); font-weight: 700; font-size: 17px;
  }
</style>
</head>
<body>
  <main class="flyer">
    <section class="hero">
      <div class="brand">
        <span class="brand-dot"></span>
        <span class="brand-name">Kempler Auction Service</span>
      </div>
      <h1 class="headline">Now Accepting Upcoming Consignments!</h1>
      <div class="auction-banner">Farm &amp; Construction Equipment<br>Auction – April 14-17</div>
      <p class="intro">Turn your equipment into cash! Get top exposure and competitive commission rates.</p>
      <div class="equipment-photo" role="img" aria-label="Green farm tractor, yellow wheel loader and yellow excavator on a plowed field under a clear sky"></div>
      <p class="online-tag">Online Auction &nbsp;|&nbsp; April 14-17</p>
    </section>

    <h2 class="rates-title">Commission Rates</h2>
    <table class="rates-table">
      <tr><th>Item Price</th><th>Commission Rate</th></tr>
      <tr><td>$1-$500</td><td>10%</td></tr>
      <tr><td>$501-$7000</td><td>8%</td></tr>
      <tr><td>$7000 and up</td><td>Flat $ 500 fee per item</td></tr>
    </table>

    <p class="custom-rates">Custom Rates Available - <span class="accent">Contact Us!</span></p>
    <div class="consign-button">Consign Now</div>
    <p class="more-items">Have more items? Contact us for custom commission rates and trucking options. We make it easy to sell!</p>

    <footer class="contact-bar">
      <span>GARRETT</span>
      <span>(555)-214-7630</span>
      <span>Garrett@kemplerauction.com</span>
    </footer>
  </main>
</body>
</html>
```